Flyer for corporate discount for dog daycare

I own a dog daycare with a large corporate down the road. I am working with the President of the company to offer their employees a discount for my services, Dog Daycare, Overnight Care, Grooming Salon & Spa and Retail. The design should be professional but also have a soft side as people view their dogs similar to human children.

I attached my logo along with our grooming brochure for reference on colors we've been using.

At a minimum the flyer must contain the following information:
Name: The Wagtail Lodge
web address: www.PawHavenStays.example
phone number: 920-555-0148
Address: 4872 Larchmont Lane
Google Map of our location

Title of flyer/program: Corporate V.I.P. (Very Important Pooch) (Can be creative with how to include this such as, Welcome to our Corporate. . .. etc.)

The program offer is: 5% discount
My services: Dog Daycare, Overnight Care, Grooming Salon & Spa and Retail

Target Market(s)

corporate employees, male and female, age 24+

Industry/Entity Type

Daycare

Requirements
Must have
• Must be easy to read and inviting.
Nice to have
• Nice photo dogs playing or inviting photo of dog.
Should not have
• cartoon feel

```html
<!DOCTYPE html>
<html lang="en">
<head>
<meta charset="utf-8">
<title>The Wagtail Lodge – Corporate V.I.P. Brochure</title>
<link rel="stylesheet" href="https://fonts.googleapis.com/css2?family=Didact+Gothic&family=Questrial&display=swap">
<style>
:root{
  --bg:#ece6dc;
  --paper:#ffffff;
  --green:#9cc83a;
  --green-text:#7aa324;
  --blue:#a9dde4;
  --ink:#3c3c3c;
  --ink-soft:#555;
  --red:#d8262e;
  --photo-a:#c9b98a;
  --photo-b:#6f7d3e;
  --map-a:#dfe9d2;
  --map-b:#c6dde3;
}
*{box-sizing:border-box;margin:0;padding:0}
html,body{width:1200px;height:800px;overflow:hidden}
body{background:var(--bg);font-family:"Didact Gothic",sans-serif;color:var(--ink);position:relative}

/* Front cover panel */
.cover{position:absolute;left:24px;top:40px;width:280px;height:720px;background:var(--green);overflow:hidden}
.cover-waves{position:absolute;inset:0}
.cover-title{position:absolute;left:22px;top:36px;width:250px;font-family:"Questrial",sans-serif;font-weight:400;font-size:32px;line-height:1.18;color:#3a3a3a}
.cover-photo{position:absolute;left:0;top:165px;width:280px;height:400px;background:linear-gradient(160deg,#b9d7e6 0%,var(--photo-a) 35%,var(--photo-b) 100%)}
.discount-badge{position:absolute;left:58px;top:462px;width:104px;height:104px;border-radius:50%;background:var(--red);border:4px solid #fff;color:#fff;text-align:center;font-family:"Questrial",sans-serif;transform:rotate(-18deg);display:flex;flex-direction:column;justify-content:center}
.discount-badge .pct{font-size:26px;line-height:1}
.discount-badge .word{font-size:17px;letter-spacing:1px}
.cover-contact{position:absolute;left:0;bottom:26px;width:100%;text-align:center;color:#fff;font-family:"Questrial",sans-serif}
.cover-contact .web{font-size:15px;margin-bottom:8px}
.cover-contact .phone{font-size:19px;margin-bottom:6px}
.cover-contact .address{font-size:13px}

/* Inside spread */
.spread{position:absolute;left:324px;top:40px;width:852px;height:720px;background:var(--paper);display:grid;grid-template-columns:repeat(3,1fr);gap:22px;padding:20px 24px 30px}
.spread::after{content:"";position:absolute;left:0;right:0;bottom:0;height:18px;background:var(--green)}
.col{font-size:8.9px;line-height:1.3;color:var(--ink-soft)}
.bar{font-family:"Questrial",sans-serif;font-weight:400;font-size:12px;letter-spacing:.5px;padding:3px 8px;margin:0 0 6px;text-transform:uppercase}
.bar-green{background:var(--green);color:#fff;text-align:center}
.bar-blue{background:var(--blue);color:#2e3b3d}
.item-title{color:var(--green-text);font-weight:bold;font-size:9px;margin-top:7px}
.col p{margin-bottom:3px}
.col ul{list-style:none;margin-bottom:5px}
.col li{padding-left:8px;position:relative}
.col li::before{content:"•";position:absolute;left:0;color:var(--green-text)}
.section-gap{margin-top:10px}

.cta{margin-top:10px;background:var(--blue);padding:5px;border-radius:8px}
.cta-inner{border:2px dashed #fff;border-radius:6px;padding:6px;display:flex;gap:8px;align-items:center;font-family:"Questrial",sans-serif;color:#2e3b3d}
.location-map{flex:0 0 70px;height:54px;border-radius:4px;background:linear-gradient(135deg,var(--map-a),var(--map-b));position:relative}
.location-map svg{position:absolute;left:27px;top:14px}
.cta-text{flex:1;text-align:center}
.cta-text .lead{font-size:10.5px}
.cta-text .num{font-size:20px;margin:2px 0}
.cta-text .address{font-size:10px}
</style>
</head>
<body>

<section class="cover" aria-label="Brochure front cover">
  <svg class="cover-waves" width="280" height="720" viewBox="0 0 280 720" aria-hidden="true">
    <rect width="280" height="720" fill="#9cc83a"/>
    <path d="M0 0H280V150C200 190 90 120 0 175Z" fill="#bfe6ec"/>
    <path d="M0 0H280V130C190 165 90 105 0 150Z" fill="#d6efbf"/>
  </svg>
  <h1 class="cover-title">Welcome to our Corporate V.I.P.</h1>
  <div class="cover-photo" role="img" aria-label="Photo of two spaniels sitting in a sunny grass field"></div>
  <svg class="cover-waves" width="280" height="720" viewBox="0 0 280 720" aria-hidden="true">
    <path d="M0 560C90 600 190 520 280 545V720H0Z" fill="#9cc83a"/>
    <path d="M0 548C90 585 190 508 280 532V545C190 520 90 600 0 560Z" fill="#a9dde4"/>
  </svg>
  <div class="discount-badge"><span class="pct">5%</span><span class="word">DISCOUNT</span></div>
  <div class="cover-contact">
    <div class="web">www.PawHavenStays.example</div>
    <div class="phone">920-555-0148</div>
    <div class="address">4872 Larchmont Lane</div>
  </div>
</section>

<section class="spread" aria-label="Brochure inside spread">
  <div class="col">
    <h2 class="bar bar-green">Daycare</h2>
    <div class="item-title">Benefits of Dog Daycare at The Wagtail Lodge</div>
    <ul>
      <li>Provides physical activity, exercise and stimulation</li>
      <li>Increased social skills</li>
      <li>Decreased destructive behaviors due to boredom</li>
      <li>Builds confidence in timid or fearful dogs</li>
      <li>Offers a safe and controlled environment for appropriate play</li>
    </ul>
    <p>Daycare is available any day during our regular business hours. We offer half days for up to five hours of play starting at $14.25 and full days of play starting at $19.25.</p>

    <h2 class="bar bar-green section-gap">Overnight Care</h2>
    <div class="item-title">Amenities</div>
    <ul>
      <li>Playtime – Guests have the opportunity to participate in our daycare program.</li>
      <li>Large climate controlled accommodations with air purification systems.</li>
      <li>Custom Meals – You bring your food from home so that your dog can enjoy his favorite meals every day.</li>
      <li>Special Care – From treats to one-on-one playtime, we offer a host of extra activities for even the most discerning pup.</li>
      <li>Pets in the same family can stay together.</li>
      <li>Access to our full range of grooming services and spa packages</li>
      <li>Pick-up and Drop-off services available for busy dog owners.</li>
    </ul>
    <div class="item-title">Pricing</div>
    <p>Overnight rates start at $36.50 per night. The cost of overnight care, however, will vary based on custom services. Additional pets sharing the same suite receive a discounted rate.</p>

    <h2 class="bar bar-green section-gap">Grooming</h2>
    <h3 class="bar bar-blue">Base Services</h3>
    <p>Your pet's experience begins with a Base Service. Rates vary by breed, size and coat condition. Call us today for an estimate.</p>
    <div class="item-title">Basic</div>
    <p>Basic shampoo, rinse, blow dry and brushing.</p>
    <div class="item-title">Essential Groom</div>
    <p>A gentle massaging, cleansing bathing process along with a luxurious towel wrap, blow dry and brushing. Includes nail clipping and ear cleaning.</p>
    <div class="item-title">Essential Style</div>
    <p>An Essential Groom followed by a hair trim to owner's specifications with a Wagtail Lodge salon professional.</p>
  </div>

  <div class="col">
    <h3 class="bar bar-blue">Enriching Shampoos</h3>
    <div class="item-title">Organic Italian Milk &amp; Vanilla: $5</div>
    <p>Moisturize, soothe and rejuvenate your pup with a luxurious milk bath that will create a glistening, shiny coat and soft skin.</p>
    <div class="item-title">Organic Italian Honey Oatmeal: $5</div>
    <p>Wonderful for pets with sensitive skin. This treatment soothes, heals and helps skin retain moisture.</p>
    <div class="item-title">Organic Olive Oil: $5</div>
    <p>A deeply moisturizing organic blend that leaves fur clean and sparkly and is perfect for pets and their humans with sensitive noses.</p>
    <div class="item-title">Organic Almond &amp; Shea Butter: $5</div>
    <p>Boosted with shea butter's superior moisturizing properties, this blend protects against dry skin and fights off flakiness, leaving your pet with a luxuriously radiant coat.</p>
    <div class="item-title">Flea &amp; Tick Bath: $5</div>
    <p>A natural and non-toxic alternative to guarding against fleas, ticks, lice and mosquitos using a wonderful blend of essential oils and gentle cleansers.</p>

    <h3 class="bar bar-blue section-gap">Soothing Conditioner</h3>
    <div class="item-title">Organic Oatmeal &amp; Honey: $5</div>
    <p>Designed to soothe, comfort and bring a healthy radiance to fur, this blend of oatmeal, honey and butter work together to create a tangle free, ultra-soft and shiny coat.</p>

    <h3 class="bar bar-blue section-gap">Spa Packages</h3>
    <p>Enhance your pups experience and health with a Spa Package. Rates are in addition to Base Service fees.</p>
    <div class="item-title">Refresh: $12</div>
    <p>Choice of enriching organic shampoo and soothing conditioner, followed by a relaxing Mango Meringue Massage.</p>
    <div class="item-title">Renew: $15</div>
    <p>Renew begins with a deep cleanse with your choice of Enriching Shampoo &amp; Soothing Conditioner, followed by a Mango Meringue Massage infused with Vitamin E that will deeply moisturize and nourish dry paws, noses and elbows. The Renew experience finishes with a Dental Care treatment leaving your pet's mouth fresh and clean.</p>
    <div class="item-title">Rejuvenate: $18</div>
    <p>The Rejuvenate experience begins with a deep coat cleanse using your choice of our all natural enriching shampoos and soothing conditioners, followed by an all-natural organic Mango Meringue Massage infused with Vitamin E that will</p>
  </div>

  <div class="col">
    <p>deeply moisturize and nourish dry paws, noses and elbows. After, your pet will enjoy a Dental Care treatment that will leave their mouth fresh and clean. A Cleansing Facial and Massage with our gentle botanical formula of oatmeal and blueberries complete this indulgent experience.</p>
    <div class="item-title">Spa Day: $14.50</div>
    <p>Few things in life are more enjoyable than a day at the spa! Your pet will spend the morning playing and socializing in daycare and the afternoon being pampered in our day spa. If your pet prefers individual attention or playtime, pampering pet sessions can be enjoyed in place of daycare.</p>

    <h3 class="bar bar-blue section-gap">Signature Spa Services</h3>
    <p>Rates are in addition to Base Service fees. To give your pet the ultimate spa experience, add a Signature Service to any Spa Package. Rates will be adjusted when added to a package.</p>
    <div class="item-title">Whipped Shea Butter Conditioning Massage: $5-10</div>
    <p>Your pet will enjoy a full body massage while this all natural, ultra-rich deep conditioning treatment moisturizes and conditions fur. Colloidal oatmeal, comfrey and aloe work together to soothe and heal dry, itchy, and irritated skin. Remarkable shine and softness will be brought back to even the most damaged coat.</p>
    <div class="item-title">Soothing Mineral Mud Bath &amp; Massage: $10</div>
    <p>This pampering experience is perfect for furry family members with sensitive skin or those suffering from hot spots, blemishes or other irritations. Mineral rich, all natural soothing relief promotes healthy cell regeneration, eases irritation related to itchy skin and hydrates your pet's coat and restores its natural radiance.</p>
    <div class="item-title">SHED-LESS Spa Package: Starting at $15</div>
    <p>During this wonderful treatment dead hair and dander are removed to promote healthy skin. A blend of natural ingredients enriched with Omega 3 &amp; 6 Fatty Acids, Calendula Extract and Papaya Leaf Extract helps reduce shedding up to 80%. Products used during service contain no parabens, artificial colors or chemical dyes. Shed-Less Treatments do not stop the natural shedding process, nor is this a one-time cure. Best results are achieved with regular service every six weeks. Speak with our salon professional about our Shed-Less Maintenance Program and discounted rates.</p>

    <div class="cta">
      <div class="cta-inner">
        <div class="location-map" role="img" aria-label="Map showing The Wagtail Lodge at 4872 Larchmont Lane">
          <svg width="16" height="22" viewBox="0 0 16 22" aria-hidden="true"><path d="M8 0C3.6 0 0 3.5 0 7.9 0 13.5 8 22 8 22s8-8.5 8-14.1C16 3.5 12.4 0 8 0Z" fill="#d8262e"/><circle cx="8" cy="8" r="3" fill="#fff"/></svg>
        </div>
        <div class="cta-text">
          <div class="lead">Schedule an Appointment Today</div>
          <div class="num">920.555.0148</div>
          <div class="address">4872 Larchmont Lane</div>
        </div>
      </div>
    </div>
  </div>
</section>

</body>
</html>
```